Design eBook cover and interior pages for vegan investment consulting firm and membership service...

I have completed an eBook that is about 6 pages of printed text (see attached PDF). I am seeking a cover page and a cool design for the interior pages. The final product should be as concise as possible while being easy to read, and not to exceed 10 pages total in any case.

My business is named Plantwise Harbor. You can learn more about the company by visiting https://plantwiseharbor.example. There, you’ll also see our current color and design choices.

We are about to start a Phase II redesign of the website, so it is not required that you match the color and style of our website. I am open to any fresh ideas regarding color, fonts, and overall aesthetic that might also inform our website redesign.

The business serves individuals “investor members” who have $50,000 or more in their investment portfolio, and also provides “purpose driven” portfolio design consulting to endowments, large asset managers, and high net worth individuals who are looking to build a vegan portfolio over $10 million or more.

Because we’re dealing with investing and people’s life savings, we want the eBook look to convey responsibility and integrity. At the same time, our audience will participate because of they are also passionate about all things vegan - protecting animals, the environment, and human health. To summarize, the goal is to have an eBook design that conveys a blend of responsibility, integrity, and passion.

Note - there is a tendency for people to first think of the color green when designing for vegan enterprises. I feel that using green as a major and even as a minor color often creates difficult or weak design outcomes. Green has become a kind of design shorthand for all things vegan and environmental, and as a result, I feel it has lost any special meaning.

Since we provide serious services to people who take investing seriously, I want color and design styles that read well, and convey responsibility, integrity and passion without relying on overused design cliches, but while still conveying a fresh perspective.

```html
<!DOCTYPE html>
<html lang="en">
<head>
<meta charset="utf-8">
<title>How Big is the Vegan Economy Today?</title>
<link href="https://fonts.googleapis.com/css2?family=Roboto:wght@300;400;700&family=Open+Sans:wght@400;600&display=swap" rel="stylesheet">
<style>
  :root {
    --brand-red: #a00b1e;
    --ink: #2a2a2a;
    --rule-soft: #d9a7ad;
    --total-bg: #f2ddd4;
    --page: #ffffff;
  }
  * { margin: 0; padding: 0; box-sizing: border-box; }
  html, body { width: 927px; height: 1200px; overflow: hidden; background: var(--page); }
  .page { position: relative; width: 927px; height: 1200px; font-family: "Open Sans", Arial, sans-serif; color: var(--ink); }

  .page-title {
    position: absolute; left: 86px; top: 96px;
    font-family: "Roboto", Arial, sans-serif; font-weight: 400;
    font-size: 43px; color: var(--brand-red); letter-spacing: -0.3px;
  }
  .title-rule { position: absolute; left: 86px; top: 156px; width: 755px; height: 1px; background: var(--brand-red); }

  .article {
    position: absolute; left: 343px; top: 342px; width: 498px;
    font-size: 15.2px; line-height: 26px; letter-spacing: 0.45px;
  }
  .article p { text-align: justify; text-indent: 26px; }
  .article p.lead { text-indent: 0; }
  .drop-cap {
    float: left; font-family: "Roboto", Arial, sans-serif; font-weight: 300;
    font-size: 80px; line-height: 66px; color: var(--brand-red);
    margin: 6px 6px 0 -4px;
  }

  .spending-table { width: 498px; border-collapse: collapse; margin-top: 14px; font-size: 14.3px; letter-spacing: 0.2px; }
  .spending-table th {
    background: var(--brand-red); color: #fff;
    font-family: "Roboto", Arial, sans-serif; font-weight: 700;
    font-size: 13.6px; line-height: 18px; letter-spacing: 0.6px; text-transform: uppercase;
    height: 51px; text-align: center; padding: 0 4px;
  }
  .spending-table th.col-category { width: 172px; }
  .spending-table td { height: 28.6px; padding: 0 6px; border-bottom: 1px solid var(--rule-soft); line-height: 1; }
  .spending-table td.amount { text-align: center; font-family: "Roboto", Arial, sans-serif; font-weight: 700; font-size: 14px; }
  .spending-table tr.total-row td { background: var(--total-bg); font-family: "Roboto", Arial, sans-serif; font-weight: 700; }
  .spending-table tr.total-row td:first-child { padding-left: 14px; }

  .closing { margin-top: 48px; }

  .footer-rule { position: absolute; left: 86px; top: 1121px; width: 755px; height: 1px; background: var(--brand-red); }
  .footer-text {
    position: absolute; left: 86px; top: 1128px; width: 755px; text-align: center;
    font-size: 14px; letter-spacing: 0.8px; color: var(--ink);
  }
</style>
</head>
<body>
<main class="page">
  <h1 class="page-title">How Big is the Vegan Economy Today?</h1>
  <div class="title-rule"></div>

  <section class="article">
    <p class="lead"><span class="drop-cap">T</span>he vegan movement has been growing by leaps and bounds. Today, there are an estimated 20 million U.S. vegans, an increase of over 500% since 2014. Similar growth is occurring in western countries as well as Asia.</p>
    <p>The U.S. Bureau of Labor Statistics reports that in 2017, the average U.S. consumer spent</p>
    <p>$60,060. Five major categories represent the immediate opportunities for growth in the vegan sector: food eaten at home, food eaten at restaurants, apparel, health care, and personal care products.</p>
    <p>This table shows how much money U.S. vegans are currently spending annually in each of these niches:</p>

    <table class="spending-table">
      <thead>
        <tr>
          <th class="col-category">Category</th>
          <th>20 Million U.S. Vegan Consumers<br>Total Annual Spending per Category</th>
        </tr>
      </thead>
      <tbody>
        <tr><td>Food at home</td><td class="amount">$87 billion</td></tr>
        <tr><td>Food at restaurants</td><td class="amount">$67 billion</td></tr>
        <tr><td>Apparel</td><td class="amount">$37 billion</td></tr>
        <tr><td>Health Care</td><td class="amount">$99 billion</td></tr>
        <tr><td>Personal Care Products</td><td class="amount">$15 billion</td></tr>
        <tr class="total-row"><td>Total</td><td class="amount">$305 billion</td></tr>
      </tbody>
    </table>

    <p class="closing">The above table shows that demand for clearly labelled vegan products is huge. To access the existing vegan market, manufacturers simply need to assure that no animals were harmed in the making of their products, and label their products appropriately as vegan friendly.</p>
  </section>

  <div class="footer-rule"></div>
  <footer class="footer-text">5 VEGAN BUSINESSES YOU SHOULD BE INVESTING IN TODAY | Page 1</footer>
</main>
</body>
</html>
```